Web design for Crowdfunding site HaloFundry.com

We need a web design for christian crowdfunding website. Here is the challenge: We need responsive layout that is targeted first in iPad size of screen. It should also scale somehow down to iPhone size of screens. Web layout can be about the same size as iPad screen.

Screens should work so that main page scrolls not but only certain part of the screen scrolls and always one "page" at time. We can implement these "scrolls" then later with javascript but now we need only design. The challenge is to create this kind of hybrid website / app look.

Target is at first to raise funds to orphan people needing about $40 per month for their living and education. There is always some organization which takes care of these kids. Later there will be other christian missions included. At first we are looking to find monthly supporters.

You can be as creative as you want :) As you see from the look and feel sector, I am not looking any same traditional look which many "help kids" sites have. I am looking to reach now younger generation and therefore iPad and mobile are the main screen sizes.

Inspirational designs:
- https://brightpixelhub.example/profiles/studiokelvira/designs/418263?from=%2Fbrowse%2Fxhr%2Fdesigns%3Fcategory%3Dmobile-app-design
- http://www.artmarketloop.example/design/7261540 Clear, simple visuals
- http://www.artmarketloop.example/design/8420917 Header
- http://www.artmarketloop.example/design/6394275 Contrast in the colors, i think is powerfull

Some terms could be: Kids play, kids are learning (in the school). No static posture but living like kids are. I wonder also how we could also add little bit gaming style even though the question is of reali life of real people. Giving should be rewarding.

Target Market(s)

People who want help other people.

Industry/Entity Type

Christian

Number of Pages Required

4 page

Requirements
Must have
• Homepage. Mission page (In my wireframes it was one kid).
Nice to have
• Other pages and some idea how to scroll. 4 pages is no must. If you feel easy, please give first some draft and I give comments on that.

```html
<!DOCTYPE html>
<html lang="en">
<head>
<meta charset="utf-8">
<title>Halo Fundry – Tablet View</title>
<link rel="stylesheet" href="https://fonts.googleapis.com/css2?family=Montserrat:wght@400;600;700;800&family=Open+Sans:wght@400;600;700&display=swap">
<style>
  :root{
    --bg:#e8ecf0;
    --ink:#1f3550;
    --navy:#17406d;
    --blue:#1f7bc4;
    --blue-deep:#0f5a9c;
    --teal:#2fb5a0;
    --green:#27a86a;
    --red:#e2474b;
    --gold:#f2b53a;
    --white:#ffffff;
    --muted:#7b8896;
    --line:#dfe5ea;
  }
  *{box-sizing:border-box;margin:0;padding:0}
  html,body{width:769px;height:1200px;overflow:hidden}
  body{background:var(--bg);font-family:"Open Sans",Arial,sans-serif;color:var(--ink);position:relative}

  .sheet-title{position:absolute;top:34px;left:0;width:100%;text-align:center;
    font-family:"Montserrat",Arial,sans-serif;font-weight:800;font-size:27px;letter-spacing:2px;color:var(--navy)}

  .screen{position:absolute;left:84px;width:600px;height:245px;background:var(--white);overflow:hidden;
    box-shadow:0 6px 18px rgba(20,50,80,.18)}
  .screen--home{top:100px}
  .screen--welcome{top:367px}
  .screen--funds{top:634px}
  .screen--events{top:901px}

  /* Home */
  .nav{height:30px;display:flex;align-items:center;padding:0 16px;background:var(--white);position:relative;z-index:2}
  .brand{display:flex;align-items:center;gap:6px;font-family:"Montserrat",sans-serif;font-weight:700;font-size:11px;color:var(--navy)}
  .brand-mark{width:12px;height:12px;background:var(--blue)}
  .nav-links{margin-left:auto;display:flex;gap:16px;font-size:7.5px;font-weight:600;color:var(--muted)}
  .nav-cta{margin-left:14px;background:var(--red);color:var(--white);font-size:7.5px;font-weight:700;padding:4px 10px;border-radius:2px}
  .hero{position:absolute;top:30px;left:0;width:600px;height:215px;
    background:linear-gradient(135deg,#c7a58a 0%,#9d7a66 35%,#6f8fa8 70%,#3f5f80 100%)}
  .hero::after{content:"";position:absolute;inset:0;background:rgba(15,40,70,.32)}
  .hero-copy{position:absolute;top:62px;width:100%;text-align:center;z-index:1;color:var(--white)}
  .hero-kicker{font-size:8px;letter-spacing:2px;font-weight:600}
  .hero-title{font-family:"Montserrat",sans-serif;font-weight:800;font-size:20px;letter-spacing:1px;margin-top:2px}
  .stats{position:absolute;top:145px;left:50%;transform:translateX(-50%);display:flex;gap:6px;z-index:1}
  .stat{width:62px;height:40px;background:rgba(255,255,255,.92);text-align:center;padding-top:6px}
  .stat b{display:block;font-family:"Montserrat",sans-serif;font-size:13px;color:var(--navy)}
  .stat span{font-size:6.5px;color:var(--muted)}
  .stat--accent{background:var(--red)}
  .stat--accent b,.stat--accent span{color:var(--white)}
  .dots{position:absolute;bottom:12px;left:50%;transform:translateX(-50%);display:flex;gap:5px;z-index:1}
  .dots i{width:6px;height:6px;border-radius:50%;background:rgba(255,255,255,.55)}
  .dots i.on{background:var(--white)}

  /* Welcome */
  .welcome-head{text-align:center;padding-top:44px}
  .welcome-head h2{font-family:"Montserrat",sans-serif;font-weight:600;font-size:16px;color:var(--ink)}
  .welcome-head p{font-size:12px;color:var(--muted);margin-top:2px}
  .steps{display:flex;justify-content:center;align-items:flex-start;margin-top:26px}
  .step{width:120px;text-align:center}
  .step-icon{width:38px;height:38px;border:2px solid var(--teal);border-radius:50%;margin:0 auto;display:flex;align-items:center;justify-content:center}
  .step h3{font-family:"Montserrat",sans-serif;font-size:7px;font-weight:700;color:var(--navy);margin-top:8px;letter-spacing:.5px}
  .step p{font-size:6.5px;color:var(--muted);margin-top:3px;line-height:1.4;padding:0 8px}
  .step-plus{width:42px;text-align:center;color:var(--teal);font-size:20px;font-weight:700;line-height:38px;position:relative}
  .step-plus::before,.step-plus::after{content:"";position:absolute;top:19px;width:10px;height:1px;background:var(--line)}
  .step-plus::before{left:0}.step-plus::after{right:0}

  /* Funds */
  .funds-title{text-align:center;font-family:"Montserrat",sans-serif;font-weight:600;font-size:16px;padding-top:16px}
  .cards{display:flex;justify-content:center;gap:14px;margin-top:12px}
  .card{width:150px;border:1px solid var(--line);background:var(--white)}
  .card-photo{height:56px}
  .card-photo--a{background:linear-gradient(135deg,#d9b69a,#9c7b65)}
  .card-photo--b{background:linear-gradient(135deg,#e4c9a2,#b88d66)}
  .card-photo--c{background:linear-gradient(135deg,#c9a487,#7d9ab0)}
  .card-body{padding:6px 8px}
  .card-name{font-family:"Montserrat",sans-serif;font-size:8px;font-weight:700;color:var(--navy)}
  .card-text{font-size:6px;color:var(--muted);margin-top:2px;line-height:1.35}
  .card-stats{display:flex;align-items:center;gap:8px;margin-top:6px}
  .card-stats small{font-size:6.5px;color:var(--muted);line-height:1.4}
  .card-stats small b{display:block;font-size:9px;color:var(--ink)}
  .btn{display:block;width:max-content;margin:10px auto 0;font-family:"Montserrat",sans-serif;font-size:7px;font-weight:700;
    letter-spacing:1px;padding:4px 14px;border:1px solid var(--blue);color:var(--blue)}

  /* Events */
  .screen--events{background:linear-gradient(160deg,var(--blue) 0%,var(--blue-deep) 100%)}
  .events-title{text-align:center;font-family:"Montserrat",sans-serif;font-weight:700;font-size:22px;color:var(--white);padding-top:14px}
  .event-card{width:300px;margin:14px auto 0;background:var(--white);text-align:center;padding:14px 18px 12px}
  .event-card h3{font-family:"Montserrat",sans-serif;font-weight:700;font-size:11px;color:var(--navy);letter-spacing:1px}
  .event-card p{font-size:8px;color:var(--muted);margin-top:8px;line-height:1.5}
  .countdown{display:flex;justify-content:center;gap:4px;margin-top:10px}
  .countdown div{width:36px;background:var(--green);color:var(--white);padding:4px 0}
  .countdown b{display:block;font-family:"Montserrat",sans-serif;font-size:11px}
  .countdown span{font-size:5.5px;letter-spacing:.5px}
  .btn--light{border-color:var(--white);color:var(--white);margin-top:12px}
</style>
</head>
<body>
  <h1 class="sheet-title">HALO FUNDRY WEBSITE TABLET VIEW</h1>

  <section class="screen screen--home">
    <nav class="nav">
      <div class="brand"><span class="brand-mark"></span>HALO FUNDRY</div>
      <div class="nav-links"><span>HOME</span><span>ABOUT</span><span>MISSIONS</span><span>EVENTS</span></div>
      <span class="nav-cta">DONATE</span>
    </nav>
    <div class="hero" role="img" aria-label="Photo of a smiling family with children"></div>
    <div class="hero-copy">
      <div class="hero-kicker">WELCOME TO</div>
      <div class="hero-title">OUR LITTLE ANGELS</div>
    </div>
    <div class="stats">
      <div class="stat stat--accent"><b>$40</b><span>per month</span></div>
      <div class="stat"><b>75</b><span>kids</span></div>
      <div class="stat"><b>171</b><span>donors</span></div>
      <div class="stat"><b>98%</b><span>funded</span></div>
    </div>
    <div class="dots"><i class="on"></i><i></i><i></i></div>
  </section>

  <section class="screen screen--welcome">
    <div class="welcome-head">
      <h2>Welcome to Halo Fundry</h2>
      <p>its a crowdfunding</p>
    </div>
    <div class="steps">
      <div class="step">
        <div class="step-icon"><svg width="18" height="18" viewBox="0 0 24 24"><path d="M12 21s-8-5-8-11a4.5 4.5 0 0 1 8-2.8A4.5 4.5 0 0 1 20 10c0 6-8 11-8 11z" fill="none" stroke="#2fb5a0" stroke-width="2"/></svg></div>
        <h3>CHOOSE A KID</h3>
        <p>Find a child whose story speaks to your heart.</p>
      </div>
      <div class="step-plus">+</div>
      <div class="step">
        <div class="step-icon"><svg width="18" height="18" viewBox="0 0 24 24"><circle cx="12" cy="12" r="8" fill="none" stroke="#2fb5a0" stroke-width="2"/><path d="M12 7v10M9 10h5a2 2 0 0 1 0 4H10" fill="none" stroke="#2fb5a0" stroke-width="2"/></svg></div>
        <h3>GIVE MONTHLY</h3>
        <p>Small gifts every month change a whole life.</p>
      </div>
      <div class="step-plus">+</div>
      <div class="step">
        <div class="step-icon"><svg width="18" height="18" viewBox="0 0 24 24"><path d="M4 20l6-6 4 4 6-8" fill="none" stroke="#2fb5a0" stroke-width="2"/><path d="M16 10h4v4" fill="none" stroke="#2fb5a0" stroke-width="2"/></svg></div>
        <h3>WATCH THEM GROW</h3>
        <p>Follow their progress at school and at play.</p>
      </div>
    </div>
  </section>

  <section class="screen screen--funds">
    <h2 class="funds-title">Popular at Funds</h2>
    <div class="cards">
      <article class="card">
        <div class="card-photo card-photo--a" role="img" aria-label="Photo of a young girl"></div>
        <div class="card-body">
          <div class="card-name">Maria, 7</div>
          <div class="card-text">Loves drawing and wants to be a teacher.</div>
          <div class="card-stats">
            <svg width="30" height="30" viewBox="0 0 36 36"><circle cx="18" cy="18" r="14" fill="none" stroke="#dfe5ea" stroke-width="4"/><circle cx="18" cy="18" r="14" fill="none" stroke="#2fb5a0" stroke-width="4" stroke-dasharray="66 88" transform="rotate(-90 18 18)"/><text x="18" y="21" font-size="8" text-anchor="middle" fill="#1f3550" font-family="Open Sans,sans-serif" font-weight="700">75%</text></svg>
            <small><b>$40</b>per month</small>
          </div>
        </div>
      </article>
      <article class="card">
        <div class="card-photo card-photo--b" role="img" aria-label="Photo of a smiling child"></div>
        <div class="card-body">
          <div class="card-name">Samuel, 9</div>
          <div class="card-text">Plays football and dreams of building bridges.</div>
          <div class="card-stats">
            <svg width="30" height="30" viewBox="0 0 36 36"><circle cx="18" cy="18" r="14" fill="none" stroke="#dfe5ea" stroke-width="4"/><circle cx="18" cy="18" r="14" fill="none" stroke="#f2b53a" stroke-width="4" stroke-dasharray="44 88" transform="rotate(-90 18 18)"/><text x="18" y="21" font-size="8" text-anchor="middle" fill="#1f3550" font-family="Open Sans,sans-serif" font-weight="700">50%</text></svg>
            <small><b>$40</b>per month</small>
          </div>
        </div>
      </article>
      <article class="card">
        <div class="card-photo card-photo--c" role="img" aria-label="Photo of a boy at school"></div>
        <div class="card-body">
          <div class="card-name">Lucas, 6</div>
          <div class="card-text">Just started school and loves reading stories.</div>
          <div class="card-stats">
            <svg width="30" height="30" viewBox="0 0 36 36"><circle cx="18" cy="18" r="14" fill="none" stroke="#dfe5ea" stroke-width="4"/><circle cx="18" cy="18" r="14" fill="none" stroke="#1f7bc4" stroke-width="4" stroke-dasharray="79 88" transform="rotate(-90 18 18)"/><text x="18" y="21" font-size="8" text-anchor="middle" fill="#1f3550" font-family="Open Sans,sans-serif" font-weight="700">90%</text></svg>
            <small><b>$40</b>per month</small>
          </div>
        </div>
      </article>
    </div>
    <span class="btn">SEE MORE</span>
  </section>

  <section class="screen screen--events">
    <h2 class="events-title">Upcoming Events</h2>
    <div class="event-card">
      <h3>FUNDRAISING SEMINAR</h3>
      <p>Pellentesque pharetra sapien non<br>quam placerat vestib sapien<br>pharetra</p>
      <div class="countdown">
        <div><b>08</b><span>DAYS</span></div>
        <div><b>14</b><span>HOURS</span></div>
        <div><b>36</b><span>MIN</span></div>
        <div><b>52</b><span>SEC</span></div>
      </div>
    </div>
    <span class="btn btn--light">SEE MORE</span>
  </section>
</body>
</html>
```